RKT Capability Statement Brochure

We need a four or six-page flyer/brochure for our capability statement. This should include all the key written copy and photos/descriptions of the personnel, plus contact addresses in the current capability statement which is attached. We are looking for a modern, professional design that matches our professional approach to our business. Please incorporate our logo into the design.

Target Market(s)

Government departments, shipping companies, port operators, lawyers, export and import businesses, commodity companies.

Industry/Entity Type

Business Consultant

Contact Information for Business Card

Professional, simple to read, uncomplicated.

Font styles to use
Serif
Sans Serif

Colors

Designer to choose colors to be used in the design.

Requirements
Must have
• Company logo
• KEY MESSAGE: Providing independent, expert, confidential and professional services.
• Description of company
• Description and photos of personnel.
• Contact details.
Should not have
• No cliches

```html
<!DOCTYPE html>
<html lang="en">
<head>
<meta charset="utf-8">
<title>RKT Capability Statement 2017</title>
<link href="https://fonts.googleapis.com/css2?family=Open+Sans:wght@400;600;700;800&display=swap" rel="stylesheet">
<style>
:root{
  --navy:#1f4785;
  --navy-dark:#142d5e;
  --ink:#2b2f3a;
  --grey:#8a8f99;
  --paper:#ffffff;
  --bg:#3a3b3d;
  --photo-blue:#6f88ad;
  --photo-grey:#c9ccd2;
}
*{margin:0;padding:0;box-sizing:border-box}
html,body{width:1200px;height:1200px;overflow:hidden;background:var(--bg);font-family:'Open Sans',Arial,sans-serif;color:var(--ink)}
.spread{position:absolute;left:204px;width:792px;height:560px;display:flex;box-shadow:0 6px 20px rgba(0,0,0,.45)}
.spread.outside{top:30px}
.spread.inside{top:610px}
.panel{position:relative;width:264px;height:560px;overflow:hidden;background:var(--paper)}
.panel.blue{background:var(--navy);color:#fff}
.panel svg.bg{position:absolute;inset:0}
.copy{position:absolute;font-size:5.6px;line-height:1.45}
.copy p{margin-bottom:4px}
.photo{position:absolute;background:linear-gradient(160deg,var(--photo-blue),var(--navy-dark))}
.photo.light{background:linear-gradient(160deg,#dfe2e7,var(--photo-grey))}
.name{font-size:7px;font-weight:700;color:#9fb5d8;font-style:normal}
.panel:not(.blue) .name{color:var(--navy)}
h3{font-size:8px;font-weight:700;color:var(--navy);margin-bottom:3px}
.blue h3{color:#a9bfe2}
.logo{position:absolute;display:flex;align-items:center;gap:5px;font-weight:800;color:var(--navy);letter-spacing:1px}
.logo .mark{width:14px;height:14px;background:var(--navy)}
.logo small{display:block;font-size:5px;font-weight:400;letter-spacing:1.5px;color:var(--grey)}
ul.list{list-style:none}
ul.list li{padding-left:7px;position:relative;margin-bottom:1.5px}
ul.list li::before{content:"";position:absolute;left:0;top:2.5px;width:3px;height:3px;border-radius:50%;background:#a9bfe2}
.cover-title{position:absolute;left:40px;top:72px;font-size:10px;font-weight:700;color:var(--navy-dark);letter-spacing:.5px}
.cover-year{position:absolute;left:96px;top:86px;font-size:22px;font-weight:800;color:var(--navy)}
.tagline{position:absolute;left:22px;top:420px;font-size:13px;line-height:1.3;font-weight:600;color:#fff}
.tagline span{color:#9aa9c2}
.cover-email{position:absolute;left:60px;top:520px;font-size:7px;color:#dbe4f3;letter-spacing:.5px}
.contacts h3{font-size:7px;text-align:center}
.contacts .region{font-size:6.2px;font-weight:700;color:var(--navy);margin-top:5px}
.contacts b{font-size:5.8px}
.icon{display:inline-block;width:5px;height:5px;background:var(--navy);border-radius:1px;margin-right:3px;vertical-align:middle}
</style>
</head>
<body>

<!-- OUTSIDE: back panel, contacts panel, cover -->
<section class="spread outside">
  <div class="panel blue team-back">
    <svg class="bg" width="264" height="560" viewBox="0 0 264 560">
      <path d="M0 440 Q120 360 264 420 V560 H0 Z" fill="#fff"/>
      <path d="M0 440 Q120 360 264 420" fill="none" stroke="#fff" stroke-width="3"/>
    </svg>
    <div class="photo" style="left:16px;top:30px;width:56px;height:62px" role="img" aria-label="Portrait of Alan Trevor"></div>
    <div class="copy" style="left:80px;top:28px;width:168px">
      <p>Based in Hobart, Alan commenced his maritime career as a deck officer, gaining a broad range of experience on many trading vessels. He later moved ashore into port operations, fleet management and marine consultancy work for the wider region.</p>
      <p>Alan has worked for shipping lines, ports and government agencies, managing safety systems, audits and vessel certification across several jurisdictions.</p>
    </div>
    <div class="copy" style="left:16px;top:96px;width:232px">
      <p><span class="name">Alan Trevor</span> — management, port logistics, bulk materials handling, safety management, ISO 9001, 14001 and 18001 auditing, and managed marine qualifications for major shipping organisations.</p>
    </div>
    <div class="photo" style="left:16px;top:150px;width:56px;height:62px" role="img" aria-label="Portrait of Mark Dunley"></div>
    <div class="copy" style="left:80px;top:148px;width:168px">
      <p>Based in Brisbane, Mark has a seafaring background and over forty years of commercial shipping experience. A Fellow of a chartered shipbrokers institute, he has owned and operated bulk and container vessels throughout the region and is a principal of a regional chartering business.</p>
      <p>Mark advises owners and charterers on commercial and consultancy services to the shipping industry.</p>
    </div>
    <div class="copy" style="left:16px;top:218px;width:232px">
      <p><span class="name">Mark Dunley</span> — operational shipping matters and chartering; part of the Ridgeline Keel Group.</p>
      <h3 style="margin-top:8px">CLIENTS</h3>
      <p>RKT's clientele includes government agencies, all of the major Australian based resource companies, ports, oil and gas operators, commercial shipping and shipper interests, as well as prominent financial institutions and business conglomerates.</p>
      <p>RKT specialises in commercial marine advice and the provision of management support in high-value marine projects. As such, RKT has won the confidence of several Commonwealth Government departments, including Defence, Customs and Border Protection and the national maritime safety authority.</p>
    </div>
    <div class="photo" style="left:0;top:415px;width:264px;height:145px;background:linear-gradient(170deg,#dfe6ef 0%,#8ea3c2 55%,#2c4d80 100%);clip-path:path('M0 25 Q120 -55 264 5 V145 H0 Z')" role="img" aria-label="Offshore support vessel at sea"></div>
  </div>

  <div class="panel contacts">
    <div class="copy" style="left:40px;top:24px;width:190px;text-align:center;color:var(--navy);font-weight:700;font-size:6px">RKT has acted as broker for significant multimillion-dollar ship acquisitions for the nation and provided advice and analysis on projects ranging from market research through to sale of surplus marine assets.</div>
    <div class="photo light" style="left:0;top:70px;width:264px;height:110px;background:linear-gradient(180deg,#fff,#e3e5ea 50%,#fff)" role="img" aria-label="Faded photo of a team shaking hands"></div>
    <div class="copy" style="left:20px;top:195px;width:224px">
      <h3>CONTACTS</h3>
      <div style="display:flex;gap:14px">
        <div style="width:105px">
          <div class="region">Victoria</div>
          <b>Ian Pressey</b><br><span class="icon"></span>+61 400 111 201<br><span class="icon"></span>ian@ridgelinekeel.com
          <div class="region">New South Wales</div>
          <b>Colin Ashby</b><br><span class="icon"></span>+61 400 111 202<br><span class="icon"></span>colin@ridgelinekeel.com
          <div class="region">Queensland</div>
          <b>Mark Dunley</b><br><span class="icon"></span>+61 400 111 203<br><span class="icon"></span>mark@ridgelinekeel.com
        </div>
        <div style="width:105px">
          <div class="region">Victoria</div>
          <b>Neil Carrow</b><br><span class="icon"></span>+61 400 111 204<br><span class="icon"></span>neil@ridgelinekeel.com
          <div class="region">Tasmania</div>
          <b>Alan Trevor</b><br><span class="icon"></span>+61 400 111 205<br><span class="icon"></span>alan@ridgelinekeel.com
        </div>
      </div>
    </div>
    <div class="logo" style="left:140px;top:388px;font-size:20px"><span class="mark"></span><div>RKT<small>RIDGELINE KEEL GROUP</small></div></div>
    <div class="copy" style="left:20px;top:430px;width:120px">
      <b style="font-size:6px">Ridgeline Keel Group Pty Ltd.<br>Atf RKT Group Unit Trust</b><br>ABN: 00 000 000 000
      <p style="margin-top:5px"><b>Registered Address:</b><br>Ridgeline Keel Group Pty Ltd,<br>42 Harbour Lane,<br>Seaview,<br>Victoria 3900</p>
    </div>
    <div class="copy" style="left:150px;top:450px;width:110px">
      <span class="icon"></span>+61 3 9000 1100<br><span class="icon"></span>+61 3 9000 1101<br><span class="icon"></span>info@ridgelinekeel.com
    </div>
  </div>

  <div class="panel blue cover">
    <svg class="bg" width="264" height="560" viewBox="0 0 264 560">
      <path d="M0 0 H264 V300 Q230 400 120 400 Q40 398 10 340 L0 330 Z" fill="#fff"/>
      <path d="M14 0 Q-10 240 120 398" fill="none" stroke="var(--navy)" stroke-width="6"/>
      <path d="M6 0 Q-16 250 110 404" fill="none" stroke="var(--navy-dark)" stroke-width="2"/>
    </svg>
    <div class="logo" style="left:64px;top:26px;font-size:26px"><span class="mark"></span><div>RKT<small>RIDGELINE KEEL GROUP</small></div></div>
    <div class="cover-title">CAPABILITY STATEMENT</div>
    <div class="cover-year">2017</div>
    <div class="photo light" style="left:40px;top:130px;width:224px;height:255px;background:linear-gradient(180deg,#f3f4f6,#9fb0c9 60%,#5d739a);clip-path:ellipse(60% 50% at 62% 50%)" role="img" aria-label="Group of business professionals standing together"></div>
    <div class="tagline">Providing independent<br><span>EXPERT, CONFIDENTIAL</span><br>&amp; professional services</div>
    <div class="cover-email">info@ridgelinekeel.com</div>
  </div>
</section>

<!-- INSIDE: overview, competencies, team -->
<section class="spread inside">
  <div class="panel overview">
    <svg class="bg" width="264" height="560" viewBox="0 0 264 560">
      <path d="M0 430 Q150 400 264 500" fill="none" stroke="var(--navy)" stroke-width="5"/>
    </svg>
    <div class="copy" style="left:18px;top:22px;width:230px">
      <h3>Company Overview</h3>
      <p>Established in 2009, the Ridgeline Keel Group (RKT) has offices in Victoria, New South Wales, Queensland and Tasmania and aims to position itself as the leading maritime consultancy in the region.</p>
      <p>The RKT team brings together extensive commercial experience and expertise to adopt a highly business-focused approach to any technical and operational analysis it undertakes within the maritime and ports industry, particularly for customers operating in the Pacific Rim.</p>
      <p>RKT has an international network of associates, including strategic partnerships with global ports and shipping data analysts, a marine insurance specialist and a long-established shipbroking house in London.</p>
      <p>RKT provides shipping, transportation and marine industry expertise to supplement and support our clients' requirements and strategies. We provide independent, expert, confidential and professional services using reliable, dedicated, highly experienced and qualified consultants and analysts who work to fully understand customer needs and requirements and provide the agreed service deliverables on time and on budget.</p>
      <p>RKT is able to step in to a client's existing organisation and supply the skill, knowledge and services to supplement or support an existing marine operation or port project. We can also apply our expertise in support of the preparation of a submission to a tribunal or legal process.</p>
      <p>The Ridgeline Keel Group is a member of the industry bodies for freight and trade and the maritime industry, and individual directors are members of professional institutes for master mariners, logistics and shipbroking.</p>
      <p>You can count on our professional team to expertly cater to all of your commercial marine requirements. With management experience at the highest levels and an extensive combined skill set, our team is unrivalled in the region. From ship acquisition and chartering to operational, logistics and economic assessments, RKT has the dependable, efficient and cost effective solutions your business needs.</p>
    </div>
    <div class="photo" style="left:0;top:415px;width:264px;height:145px;background:linear-gradient(150deg,#f2f3f5,#b9c2cf 50%,#4b5d7c);clip-path:path('M0 20 Q150 -15 264 88 V145 H0 Z')" role="img" aria-label="Two colleagues reviewing work at a laptop"></div>
  </div>

  <div class="panel blue competencies">
    <svg class="bg" width="264" height="560" viewBox="0 0 264 560">
      <path d="M0 0 H264 V40 Q120 20 0 80 Z" fill="#fff"/>
      <path d="M0 80 Q120 20 264 40" fill="none" stroke="#a9bfe2" stroke-width="1"/>
    </svg>
    <div class="copy" style="left:16px;top:62px;width:236px">
      <div style="font-size:6px;color:#a9bfe2">Core Competencies</div>
      <h3 style="color:#fff;font-size:7px">RKT has demonstrable experience in the following areas:</h3>
      <h3>COMMERCIAL MARITIME TRADE</h3>
      <div style="display:flex;gap:10px">
        <ul class="list" style="width:112px"><li>Operational knowledge of all major shipping trades</li><li>Thorough understanding of maritime, ports and logistics policy</li><li>Reviews of commercial maritime operations</li><li>Evaluation and management of tenders and proposal preparation</li><li>Feasibility studies (commercial and operational)</li></ul>
        <ul class="list" style="width:112px"><li>Reviews of commercial maritime operations</li><li>Advice on joint venture issues and contracts</li><li>Fleet availability and trade sector forecasting</li><li>Industry education and training</li><li>Topical industry workshops</li><li>Expert witness</li></ul>
      </div>
      <h3 style="margin-top:6px">SHIP MANAGEMENT</h3>
      <div style="display:flex;gap:10px">
        <ul class="list" style="width:112px"><li>Vessel ownership and management</li><li>Vessel chartering and operational management</li><li>Vessel sales and purchase</li><li>Advice on ship charter parties</li><li>Re-engineering of marine departments</li><li>Innovative improvements to marine systems</li></ul>
        <ul class="list" style="width:112px"><li>Management of suppliers and related resource management</li><li>Managing the shipping and logistic requirements of companies</li><li>Analysing and meeting ship charterers' needs from ship acquisition to cargo delivery</li></ul>
      </div>
      <h3 style="margin-top:6px">PORTS &amp; RELATED INDUSTRY</h3>
      <div style="display:flex;gap:10px">
        <ul class="list" style="width:112px"><li>Modelling and optimisation of port throughput</li><li>Matching port infrastructure to commodity types and volumes</li><li>Management of port loading and unloading terminals</li><li>Planning and management of the ship-shore interface</li><li>Port efficiency assessments</li><li>Modelling port use using queue theory</li></ul>
        <ul class="list" style="width:112px"><li>Modelling and forecasting aggregate annual demurrage charges</li><li>Assessments of port and marine safety and security</li><li>Risk assessments of marine and port operations</li><li>Reviews and assessments of navigation and marine safety</li><li>Emergency and crisis management</li></ul>
      </div>
      <h3 style="margin-top:6px">SUPPLY CHAIN</h3>
      <div style="display:flex;gap:10px">
        <ul class="list" style="width:112px"><li>Supply chain evaluation and optimisation</li><li>Evaluation and management of tenders and proposal preparation</li><li>Marine project management, project services and support</li></ul>
        <ul class="list" style="width:112px"><li>Management of bulk and breakbulk logistics</li><li>Stacking analysis for bulk terminals</li><li>Re-engineering of supply chains</li></ul>
      </div>
    </div>
  </div>

  <div class="panel team">
    <div class="copy" style="left:16px;top:20px;width:232px">
      <h3>Ridgeline Keel Group Team</h3>
      <p>All team members have decades of commercial shipping industry experience at senior levels and have substantial relevant specialist expertise to offer. With first-class reputations and extensive and diverse backgrounds, the members of the RKT team bring together a capacity unique in the region for comprehensive, evidence-based analysis and evaluation of major maritime and port projects.</p>
      <h3 style="font-size:7px">The RKT management team comprises:</h3>
    </div>
    <div class="photo" style="left:16px;top:100px;width:56px;height:62px" role="img" aria-label="Portrait of Colin Ashby"></div>
    <div class="copy" style="left:80px;top:98px;width:168px">
      <p>Based in Sydney, Colin was, prior to joining RKT, general manager of shipping for a major resources group for seventeen years, where his responsibilities included managing owned and chartered ships for the transport of raw materials. He holds degrees in science and maritime studies and is a Chartered Member of a logistics institute.</p>
    </div>
    <div class="copy" style="left:16px;top:168px;width:232px">
      <p><span class="name">Colin Ashby</span> — studies for port logistics and shipping projects; former director of a national shipowners association and a marine insurance association.</p>
    </div>
    <div class="photo" style="left:16px;top:205px;width:56px;height:62px" role="img" aria-label="Portrait of Neil Carrow"></div>
    <div class="copy" style="left:80px;top:203px;width:168px">
      <p>Based in Melbourne, Neil has more than forty years' experience in the international maritime and transport industry, including some years at sea as a deck officer. As a leading industry analyst he has been contracted to work on major projects for government agencies, ports, terminal operators and commodity companies.</p>
    </div>
    <div class="copy" style="left:16px;top:272px;width:232px">
      <p><span class="name">Neil Carrow</span> — port and shipping consultancies across the Pacific Rim; recipient of a lifetime achievement award from a master mariners society.</p>
    </div>
    <div class="photo" style="left:16px;top:310px;width:56px;height:62px" role="img" aria-label="Portrait of Ian Pressey"></div>
    <div class="copy" style="left:80px;top:308px;width:168px">
      <p>Based in Melbourne, Ian is a Master Mariner and holds an MBA and a logistics qualification. He has over forty years of experience in the shipping industry and is a founding member of RKT. Ian previously served as general manager of a shipping company and held senior positions in port development.</p>
    </div>
    <div class="copy" style="left:16px;top:378px;width:232px">
      <p><span class="name">Ian Pressey</span> — within a major resources group, Ian held senior roles in marine operations, strategic planning and project development, and was a joint venture leader on the marine elements of a number of major infrastructure projects both within Australia and internationally. He has extensive experience in analysing supply and demand scenarios and the development of business cases.</p>
    </div>
  </div>
</section>

</body>
</html>
```